Veltisa Promotions | Web Design Project

We need a web design for a new Promotion Company based in Toronto, Canada named Veltisa Promotions.

Veltisa Promotions has an idea and vision to set high standard, be EXCLUSIVE and attract a group of people that will follow us through events we promote (night clubs, brand promotions, music events, and sport events)

We want to present a high standards and classy image to the others...

layout/style of the website would be best explained by this template

http://www.quorvanlayouts.example/view-ttemplate-58147.html

Target Market(s)

male/female age 25-40 Target: business owners young entrepreneur - clubing industry - media industry - promotion industry - marketing media industry

Industry/Entity Type

It Company

Requirements
Must have
• website would have about 5 pages ... example in terms of content (http://www.brastowgroup.example/lifestyle.html)

About Veltisa
Events
Media
Promotions
Affiliates
Contact

as well as chirpnet and friendwall logo/links
newsletter section
music control

need to have a easy to view gallery page (pictures from events)
Events would have to include flyers .. for past/future events
Media - would include videos/pictures from the events

Affiliates - list of affiliates with their logos and short description..

Main Pages
background would be pictures of Toronto
it would be nice to have some kind of flash/swf
space for flyer and picture of the week...

logo file is uploaded.

```html
<!DOCTYPE html>
<html lang="en">
<head>
<meta charset="utf-8">
<title>Veltisa Promotions</title>
<link href="https://fonts.googleapis.com/css2?family=Gelasio:wght@400;500&display=swap" rel="stylesheet">
<style>
  :root {
    --bg-top: #1d5f86;
    --bg-mid: #134a6c;
    --bg-low: #0c3550;
    --footer: #04121a;
    --frame: #0b2d42;
    --panel: #dbf3fb;
    --sidebar: #b8d9e5;
    --heading: #1d9ad0;
    --body-text: #1b5877;
    --side-text: #15506d;
    --logo: #2fb4e6;
    --affil-bar: #07222e;
    --affil-tile: #6b9fb1;
    --affil-edge: #0d3446;
    --footer-text: #34515f;
    --white: #ffffff;
  }
  * { margin: 0; padding: 0; box-sizing: border-box; }
  html, body { width: 1200px; height: 742px; overflow: hidden; }
  body {
    position: relative;
    font-family: "Gelasio", Georgia, serif;
    background: linear-gradient(180deg, var(--bg-top) 0%, var(--bg-mid) 45%, var(--bg-low) 90%);
  }
  .skyline {
    position: absolute; left: 0; top: 420px; width: 1200px; height: 252px;
    background: linear-gradient(180deg, rgba(12,53,80,0) 0%, rgba(35,90,120,0.45) 55%, rgba(8,40,60,0.7) 100%);
  }
  .logo {
    position: absolute; left: 130px; top: 30px;
    display: flex; align-items: center; gap: 10px;
  }
  .logo-mark { width: 22px; height: 22px; border: 2px solid var(--logo); }
  .logo-name { color: var(--logo); font-size: 34px; letter-spacing: 1px; line-height: 1; }

  .main-nav { position: absolute; left: 510px; top: 44px; width: 570px; height: 30px; border-bottom: 1px solid #1f6c97; }
  .main-nav a {
    position: absolute; top: 3px; transform: translateX(-50%);
    color: var(--white); font-size: 13px; text-decoration: none; white-space: nowrap;
    text-shadow: 0 1px 2px rgba(0,0,0,0.5);
  }
  .main-nav a.active::before {
    content: ""; position: absolute; left: -18px; right: -18px; top: -10px; bottom: -10px;
    background: radial-gradient(ellipse at center, rgba(140,215,245,0.55) 0%, rgba(140,215,245,0) 70%);
    z-index: -1;
  }

  .content-frame { position: absolute; left: 120px; top: 110px; width: 960px; height: 452px; background: var(--frame); border-radius: 10px; }
  .about-panel { position: absolute; left: 130px; top: 120px; width: 630px; height: 432px; background: var(--panel); border-radius: 4px 0 0 4px; }
  .about-panel h1 {
    position: absolute; left: 26px; top: 20px; width: 560px;
    font-weight: 400; font-size: 29px; color: var(--heading);
    padding-bottom: 6px; border-bottom: 1px solid #c3e3ee;
    text-shadow: 0 1px 1px rgba(0,0,0,0.15);
  }
  .feature-photo {
    position: absolute; left: 25px; top: 72px; width: 275px; height: 216px;
    border: 2px solid var(--frame); border-radius: 4px;
    background: radial-gradient(circle at 55% 40%, #d8785a 0%, #8a3a2e 40%, #2a0f12 100%);
  }
  .about-panel p { position: absolute; font-size: 12.5px; line-height: 24px; color: var(--body-text); }
  .intro { left: 320px; top: 68px; width: 270px; }
  .more { left: 25px; top: 308px; width: 565px; }

  .sidebar { position: absolute; left: 760px; top: 120px; width: 310px; height: 432px; background: var(--sidebar); border-left: 1px solid #8fb8c8; border-radius: 0 4px 4px 0; }
  .spot { position: absolute; left: 30px; width: 280px; height: 120px; }
  .spot-photo { position: absolute; left: 0; top: 0; width: 140px; height: 120px; background: var(--frame); border-radius: 4px; padding: 5px; box-shadow: 0 5px 4px -2px rgba(0,0,0,0.25); }
  .spot-photo span { display: block; width: 130px; height: 110px; border-radius: 3px; }
  .spot h2 { position: absolute; left: 150px; top: 13px; font-weight: 400; font-size: 15.5px; color: var(--heading); white-space: nowrap; }
  .spot p { position: absolute; left: 150px; top: 36px; width: 110px; font-size: 12px; line-height: 12px; color: var(--side-text); }

  .affiliates { position: absolute; left: 130px; top: 576px; width: 940px; height: 72px; background: var(--affil-bar); border-radius: 4px; }
  .affiliates h2 { position: absolute; left: 30px; top: 23px; font-weight: 400; font-size: 20px; color: var(--heading); }
  .affil-tile { position: absolute; top: 13px; width: 58px; height: 46px; background: var(--affil-tile); border: 2px solid var(--affil-edge); border-radius: 4px; }

  .site-footer { position: absolute; left: 0; top: 672px; width: 1200px; height: 70px; background: var(--footer); }
  .site-footer a, .site-footer small { position: absolute; top: 28px; font-size: 12px; color: var(--footer-text); text-decoration: none; }
  .copyright { right: 130px; }
</style>
</head>
<body>
  <div class="skyline" role="img" aria-label="Faint night view of the Toronto skyline"></div>

  <header>
    <div class="logo"><span class="logo-mark"></span><span class="logo-name">Veltisa</span></div>
    <nav class="main-nav">
      <a href="#" class="active" style="left:87px">About Veltisa</a>
      <a href="#" style="left:210px">Events</a>
      <a href="#" style="left:287px">Media</a>
      <a href="#" style="left:367px">Promotions</a>
      <a href="#" style="left:449px">Affiliates</a>
      <a href="#" style="left:529px">Contact</a>
    </nav>
  </header>

  <div class="content-frame"></div>

  <main class="about-panel">
    <h1>Veltisa Promotions</h1>
    <div class="feature-photo" role="img" aria-label="Young people dancing at a club night under warm stage lights"></div>
    <p class="intro">Duis mollis, est non commodo luctus, nisi erat porttitor ligula, eget lacinia odio sem nec elit. Nullam quis risus eget urna mollis ornare vel eu leo. Cras justo odio, dapibus ac facilisis in, egestas eget quam. Nullam quis risus eget urna mollis ornare vel eu leo. Donec id elit non mi porta gravida at eget metusest non commodo luctus, nisi erat porttitor ligula. Sed posuere consectetur est at lobortis.</p>
    <p class="more">Nullam quis risus eget urna mollis ornare vel eu leo. Donec ullamcorper nulla non metus auctor fringilla. Sed posuere consectetur est at lobortis. Sed posuere consectetur est at lobortis. Vivamus sagittis lacus vel augue laoreet rutrum faucibus dolor auctor. Aenean lacinia bibendum nulla sed consectetur. Donec id elit non mi porta gravida at eget metus.</p>
  </main>

  <aside class="sidebar">
    <article class="spot" style="top:24px">
      <div class="spot-photo"><span role="img" aria-label="Group photo of the team in business attire" style="background:linear-gradient(180deg,#f4f6f7 0%,#c9ccd0 60%,#3a3f48 100%)"></span></div>
      <h2>The Team</h2>
      <p>Meet our team at headquarter</p>
    </article>
    <article class="spot" style="top:156px">
      <div class="spot-photo"><span role="img" aria-label="Portrait of a notable person in a red shirt" style="background:linear-gradient(180deg,#eef0f1 0%,#d9b4a8 55%,#b8443c 100%)"></span></div>
      <h2>Notable Person1</h2>
      <p>Back from NY to build Toronto</p>
    </article>
    <article class="spot" style="top:288px">
      <div class="spot-photo"><span role="img" aria-label="Portrait of a notable person in a dark shirt" style="background:linear-gradient(180deg,#6c6c6c 0%,#4a4a4a 50%,#151515 100%)"></span></div>
      <h2>Notable Person2</h2>
      <p>There's always a fun night every week</p>
    </article>
  </aside>

  <section class="affiliates">
    <h2>Affiliates</h2>
    <span class="affil-tile" style="left:161px"></span>
    <span class="affil-tile" style="left:241px"></span>
    <span class="affil-tile" style="left:321px"></span>
    <span class="affil-tile" style="left:401px"></span>
    <span class="affil-tile" style="left:481px"></span>
    <span class="affil-tile" style="left:561px"></span>
    <span class="affil-tile" style="left:641px"></span>
    <span class="affil-tile" style="left:721px"></span>
    <span class="affil-tile" style="left:801px"></span>
  </section>

  <footer class="site-footer">
    <a href="#" style="left:142px">Chirpnet</a>
    <a href="#" style="left:215px">Friendwall</a>
    <small class="copyright">Copyright Veltisa Promotion, all rights reserved</small>
  </footer>
</body>
</html>
```